Brindlewood Debating Uniform - Double Sided A4 flyer - Adobe Photoshop needed

We need a double sided flyer to "sell" the concept of a new debating uniform with kilts for Brindlewood Grammar School.

Front Page
=========

- Title "A Debating Uniform for Brindlewood?"
- large, Brindlewood Grammar Logo (see attachment),
- photo of a single debater in action (a boy mid teens speaking to an audience) wearing new uniform - YOU WILL NEED TO SOURCE THIS AND EDIT UNIFORM
- Text box. text to say:

Why does Brindlewood Grammar need a debating uniform?
- Brindlewood has had unparalleled success in debating recently and has lifted its profile enormously reaching the PLVC finals this year
- debating is now beginning to be seen as a key school sport with a growing group of participants and supporters
- first impressions are important in debating and our teams often arrive in different uniforms
- as Friday is cadet corps day some debaters wear cadet uniform (which may, depending on the day, be regular camouflage or ceremonial uniform with kilts, or a mixture) and some wear regular school uniform, some with blazers on and some with them off
- this is in contrast to other schools whose appearance is usually identical and impeccable

Why kilted?
- Distinctive!
- strong school tradition
- the Galloran tartan is one of the key insignias of Brindlewood Grammar School
- Highly Photogenic! Will draw more attention to the teams in the public eye and in the press
- boys like wearing them, they are cool
- will draw further interest in debating from potential participants
- the boys are used to wearing kilts
- Intimidating to the opposition in the greatest Scottish tradition!

And remember "A man in a kilt is a man and a half!"

=========================================
The rear side needs a picture of the three kilted men walking along
- you can use this picture attached or another but the men need to be YOUNG with short hair and and no beards or moustaches
- their kilts need to be changed to the Galloran Tartan (attached)
- their jackets need to be changed to Brindlewood blazers in Royal Blue with school insignia on pocket. Note piping. Keep the cut of the jacket the same as in the 3 men photo.
- their ties need to be changed to school ties (dar bluw ith royal blue diagonal stripes)
- the three figures to have different waistcoats (vests)
- one with a bright red waistcoat, one with royal blue waistcoat matching the blazer and one with no waistcoat at all, just a white shirt under the jacket

==================================
TEXT BOX AS BELOW

The proposal:
- a debating uniform will be worn by all [senior] debaters
- this will comprise:
- a school kilt in the Galloran tartan
- thistle kilt pin
- black kilt belt with silver thistle buckle
- a plain black and silver leather sporran (not the horsehair sporrans which are more military)
- a white shirt
- school tie
- school blazer cut down to kilt jacket size
- possibly a waistcoat in royal blue or red (for discussion)
- dark hose
- black shoes

There is a large supply of the Galloran tartan kilts available. The only items which would need to be sourced are the sporrans, belts, hose and cut down blazers. Old blazers can be recut to be suitable as kilt jackets, this is not a major exercise.

===================================
Updates

THIS STYLE OF PHOTO WOULD BE GOOD FOR THE FRONT BUT YOU WILL HAVE TO RECLOTHE HIM IN KILT, BLAZER AND TIE

PLEASE SEE THE SCHOOL WEBSITE

WWW.BRINDLEWOOD.EXAMPLE.EDU.AU FOR FURTHER IMAGES

Hi all,

I have received a few designs but none with the kilt pictures photoshopped.  Please read the brief.  The three guys walking along in kilts need to have the tartan changed to the one attached. Their jackets need to be turned into royal blue blazers. The single speaker on the front page needs to be dressed the same.

If you can do a good job on photoshop with these then you are in the running to win this.

regards

Target Market(s)

school students and teachers

Industry/Entity Type

School

Requirements
Must have
• 2 photoshopped photos, one of single boy debating (dressed in new uniform) on FRONT and one of 3 young men walking along on BACK with the new kilts (tartan sample attached) and jackets of royal blue. Please note that the photo retouching is the most important part of this job. We need to "mock up" the new uniform.

School logo and text on front

Text on back
Nice to have
• Attention grabbing design

```html
<!DOCTYPE html>
<html lang="en">
<head>
<meta charset="utf-8">
<title>A Debating Uniform for Brindlewood?</title>
<link href="https://fonts.googleapis.com/css2?family=Poppins:wght@600;700&family=Arimo:wght@400;700&display=swap" rel="stylesheet">
<style>
  :root {
    --backdrop: #eeeeee;
    --page: #ffffff;
    --page-edge: #bdbdbd;
    --ink: #111111;
    --muted: #8a8a8a;
    --crest-blue: #1d4f9a;
    --photo-hall-top: #8a3a22;
    --photo-hall-bottom: #5a3a24;
    --photo-park-top: #6f8a4a;
    --photo-park-bottom: #b9a58a;
  }
  * { margin: 0; padding: 0; box-sizing: border-box; }
  html, body { width: 1200px; height: 852px; overflow: hidden; background: var(--backdrop); }
  body { position: relative; font-family: "Arimo", Arial, sans-serif; color: var(--ink); }

  .page {
    position: absolute; top: 22px; width: 576px; height: 812px;
    background: var(--page); border: 1px solid var(--page-edge);
  }
  .page--front { left: 14px; }
  .page--back { left: 607px; }
  .page > * { position: absolute; }

  .page-title {
    font-family: "Poppins", Arial, sans-serif; font-weight: 700;
    width: 100%; text-align: center; white-space: nowrap; line-height: 1.1;
  }
  .page--front .page-title { top: 26px; font-size: 25px; }
  .page--back .page-title { top: 10px; font-size: 32px; }

  .section-heading { font-weight: 700; font-size: 16.5px; line-height: 21px; }
  .reasons-heading { left: 14px; top: 79px; width: 280px; text-align: center; white-space: nowrap; }
  .kilt-heading { left: 234px; top: 468px; }

  .point-list { list-style: none; font-size: 11px; font-weight: 700; line-height: 13.8px; }
  .point-list li { text-align: justify; margin-bottom: 13.8px; }
  .reasons-list { left: 32px; top: 128px; width: 224px; }
  .kilt-list { left: 234px; top: 496px; width: 310px; }
  .kilt-list li { margin-bottom: 13px; line-height: 13.5px; }

  .photo { display: block; }
  .debater-photo {
    left: 291px; top: 75px; width: 262px; height: 390px;
    background: linear-gradient(160deg, var(--photo-hall-top), var(--photo-hall-bottom));
  }
  .walkers-photo {
    left: 26px; top: 51px; width: 523px; height: 530px;
    background: linear-gradient(180deg, var(--photo-park-top), var(--photo-park-bottom));
  }

  .school-mark {
    left: 40px; top: 590px; width: 160px;
    display: flex; flex-direction: column; align-items: center; gap: 12px;
  }
  .school-mark__square { width: 70px; height: 70px; background: var(--crest-blue); }
  .school-mark__name {
    font-family: "Poppins", Arial, sans-serif; font-weight: 700; font-size: 15px;
    line-height: 19px; text-align: center; color: var(--crest-blue);
  }

  .closing-line {
    left: 0; top: 768px; width: 100%; text-align: center; white-space: nowrap;
    font-family: "Poppins", Arial, sans-serif; font-weight: 600; font-size: 15px;
  }

  .proposal-lead {
    left: 0; top: 586px; width: 100%; text-align: center; white-space: nowrap;
    font-family: "Poppins", Arial, sans-serif; font-weight: 600; font-size: 15px;
  }
  .component-list {
    left: 28px; top: 619px; width: 330px; list-style: none;
    font-weight: 700; font-size: 11px; line-height: 13.8px;
  }
  .supply-note {
    left: 364px; top: 618px; width: 187px;
    font-size: 11px; line-height: 13.6px; color: var(--muted); text-align: justify;
  }
</style>
</head>
<body>

<section class="page page--front">
  <h1 class="page-title">A Debating Uniform for Brindlewood?</h1>

  <h2 class="section-heading reasons-heading">Why does Brindlewood Grammar<br>need a debating uniform?</h2>
  <ul class="point-list reasons-list">
    <li>- Brindlewood has had unparalleled success in debating recently and has lifted its profile enormously reaching the PLVC finals this year.</li>
    <li>- Debating is now beginning to be seen as a key school sport with a growing group of participants and supporters.</li>
    <li>- First impressions are important in debating and our teams often arrive in different uniforms.</li>
    <li>- As Friday is cadet corps day, some debaters wear cadet uniform (which may, depending on the day, be regular camouflage or ceremonial uniform with kilts, or a mixture) and some wear regular school uniform, some with blazers on and some with them off.</li>
    <li>- This is in contrast to other schools whose appearance is usually identical and impeccable.</li>
  </ul>

  <div class="photo debater-photo" role="img" aria-label="Photo of a teenage debater in a royal blue blazer, tie and tartan kilt speaking to an audience in a wood-panelled hall"></div>

  <h2 class="section-heading kilt-heading">Why kilted?</h2>
  <ul class="point-list kilt-list">
    <li>- Distinctive!</li>
    <li>- Strong school tradition</li>
    <li>- The Galloran tartan is one of the key insignias of Brindlewood Grammar School</li>
    <li>- Highly Photogenic! Will draw more attention to the teams in the public eye and in the press.</li>
    <li>- Boys like wearing them, they are cool.</li>
    <li>- Will draw further interest in debating from potential participants.</li>
    <li>- The boys are used to wearing kilts.</li>
    <li>- Intimidating to the opposition in the greatest Scottish tradition!</li>
  </ul>

  <div class="school-mark">
    <span class="school-mark__square"></span>
    <span class="school-mark__name">Brindlewood Grammar School</span>
  </div>

  <p class="closing-line">and remember “A man in a kilt is a man and a half!”</p>
</section>

<section class="page page--back">
  <h1 class="page-title">The Proposal:</h1>

  <div class="photo walkers-photo" role="img" aria-label="Photo of three young men walking along a park path wearing royal blue blazers, school ties, tartan kilts, sporrans and dark hose"></div>

  <p class="proposal-lead">A debating uniform will be worn by all (senior) debaters</p>

  <ul class="component-list">
    <li>This will comprise:</li>
    <li>- A school kilt in the Galloran tartan</li>
    <li>- Thistle kilt pin</li>
    <li>- Black kilt belt with silver thistle buckle</li>
    <li>- A plain black and silver leather sporran (not the horsehair sporrans which are more military)</li>
    <li>- A white shirt</li>
    <li>- School Tie</li>
    <li>- School blazer cut down to kilt jacket size</li>
    <li>- Possibly a waistcoat in royal blue or red (for discussion)</li>
    <li>- Dark hose</li>
    <li>- Black Shoes</li>
  </ul>

  <p class="supply-note">There is a large supply of the Galloran tartan kilt available. The only items which would need to be sourced are the sporrans, belts, hose and cut down blazers. Old blazers can be recut to be suitable as kilt jackets, this is not a major exercise.</p>
</section>

</body>
</html>
```